Carry The Tide Home

Business Card design

Target Market(s)

People who require support in the commnity

Industry/Entity Type

Mental Health Support

Contact Information for Business Card

Mental Health Support Rosalind Bratten carrythetidehome@mailvane.com.au 0481 637 592 PO Box 629 Wattle Reach QLD 4592

Colors
6B429C
8869AF
B7A5CE
E3DAEB
F3F0F8

Requirements
Must have
• Logo & details listed above
Should not have
• No red or orange

```html
<!DOCTYPE html>
<html lang="en">
<head>
<meta charset="utf-8">
<title>Carry The Tide Home – Business Card</title>
<link href="https://fonts.googleapis.com/css2?family=Montserrat:wght@500;600;800&display=swap" rel="stylesheet">
<style>
  :root {
    --purple: #6b429c;
    --yellow: #f2e92a;
    --ink: #1c1c1c;
    --paper: #ffffff;
    --backdrop: #e6e3ea;
  }
  * { box-sizing: border-box; margin: 0; padding: 0; }
  html, body { width: 1200px; height: 900px; overflow: hidden; }
  body {
    background: var(--backdrop);
    font-family: "Montserrat", Arial, sans-serif;
    position: relative;
  }
  .card {
    position: absolute;
    width: 620px;
    height: 354px;
    background: var(--paper);
    box-shadow: 0 6px 18px rgba(0,0,0,0.18);
    overflow: hidden;
  }
  .card--front { left: 60px; top: 70px; }
  .card--back { left: 520px; top: 476px; }

  .brand {
    position: absolute;
    display: flex;
    align-items: center;
    gap: 16px;
    color: var(--purple);
    font-weight: 600;
    white-space: nowrap;
  }
  .brand__dot {
    border-radius: 50%;
    background: var(--purple);
    flex: none;
  }
  .card--front .brand {
    left: 50%; top: 50%;
    transform: translate(-50%, -50%);
    font-size: 30px;
    letter-spacing: 0.04em;
  }
  .card--front .brand__dot { width: 74px; height: 74px; }

  .card--back .brand {
    left: 50%; top: 40px;
    transform: translateX(-50%);
    font-size: 20px;
    letter-spacing: 0.04em;
    gap: 12px;
  }
  .card--back .brand__dot { width: 48px; height: 48px; }

  .details {
    position: absolute;
    left: 0; right: 0;
    top: 130px;
    text-align: center;
  }
  .details__title {
    color: var(--purple);
    font-weight: 800;
    font-size: 17px;
    text-transform: uppercase;
    letter-spacing: -0.01em;
  }
  .details__line {
    margin-top: 8px;
    font-weight: 500;
    font-size: 15px;
    color: var(--ink);
    display: flex;
    justify-content: center;
    align-items: center;
    gap: 7px;
  }
  .details__line svg { width: 15px; height: 15px; fill: var(--purple); flex: none; }
  .details__gap { width: 6px; }

  .bands { position: absolute; left: 0; top: 0; width: 620px; height: 354px; }
</style>
</head>
<body>

  <section class="card card--front">
    <div class="brand">
      <span class="brand__dot"></span>
      <span class="brand__name">Carry The Tide Home</span>
    </div>
  </section>

  <section class="card card--back">
    <svg class="bands" viewBox="0 0 620 354" aria-hidden="true">
      <path fill="var(--purple)" d="M0,354 L0,338 L420,298 C448,295 458,282 472,272 C488,262 505,259 530,256 L620,244 L620,354 Z"/>
      <path fill="var(--yellow)" d="M0,326 L0,316 L452,268 L440,282 Z"/>
    </svg>

    <div class="brand">
      <span class="brand__dot"></span>
      <span class="brand__name">Carry The Tide Home</span>
    </div>

    <div class="details">
      <p class="details__title">Mental Health Support Rosalind Bratten</p>
      <p class="details__line">
        <svg viewBox="0 0 24 24"><path d="M12 2a7 7 0 0 0-7 7c0 5 7 13 7 13s7-8 7-13a7 7 0 0 0-7-7zm0 9.5A2.5 2.5 0 1 1 12 6.5a2.5 2.5 0 0 1 0 5z"/></svg>
        <span>PO Box 629 Wattle Reach QLD 4592</span>
      </p>
      <p class="details__line">
        <svg viewBox="0 0 24 24"><path d="M6.6 10.8a15.1 15.1 0 0 0 6.6 6.6l2.2-2.2a1 1 0 0 1 1-.25 11.4 11.4 0 0 0 3.6.57 1 1 0 0 1 1 1V20a1 1 0 0 1-1 1A17 17 0 0 1 3 4a1 1 0 0 1 1-1h3.5a1 1 0 0 1 1 1c0 1.25.2 2.45.57 3.57a1 1 0 0 1-.25 1z"/></svg>
        <span>0481 637 592</span>
        <span class="details__gap"></span>
        <svg viewBox="0 0 24 24"><path d="M3 5h18v14H3z M3 5l9 7 9-7" fill="none" stroke="var(--purple)" stroke-width="2.2"/></svg>
        <span>carrythetidehome@mailvane.com.au</span>
      </p>
    </div>
  </section>

</body>
</html>
```